Design refresh of existing HR Application

QuillStaff is an HR & Payroll processing software, already in use by thousands of people. It is a feature packed, enterprise-grade software that is also simple and user friendly. Visit us at https://quillstaff.example

Seeking a refresh of the app design/UI.

Key objectives are to make it "sleeker", more professional and polished, whist still retaining functionality. Not intended to be a massive overhaul, but more of reorganization and improvements on design elements.

You may login to our demo account to see the app live.
https://app.quillstaff.example/login
User: demo@quillstaff.example
Password: Zip20

Target Market(s)

HR Managers, business administrators/owners and employees.

Industry/Entity Type

Business Software

Number of Pages Required

4 page

Font styles to use
Other font styles liked:
• Lato

Colors
0255a3
3377b5
00a990
33b8a4
f37122
faa54b

Requirements
Must have
• Must retain the current functionality on each page.
Nice to have
• Fine to suggest changes to colors, font sizes, card designs, moving sections around and any other design element changes.

```html
<!DOCTYPE html>
<html lang="en">
<head>
<meta charset="utf-8">
<title>QuillStaff — Dashboard</title>
<link href="https://fonts.googleapis.com/css2?family=Roboto:wght@400;500;700&display=swap" rel="stylesheet">
<style>
:root{
  --page:#f2f2f2;
  --card:#ffffff;
  --side:#023f4b;
  --side-dark:#012f38;
  --side-active:#0f5361;
  --nav-label:#1b9e95;
  --nav-icon:#f3b64a;
  --teal-ink:#0b4a53;
  --ink:#1d1d1d;
  --muted:#5b5b5b;
  --soft:#b9b9b9;
  --faint:#cfcfcf;
  --orange:#f37122;
  --orange-soft:#fdf1e6;
  --blue:#0255a3;
  --line:#e4e4e4;
}
*{box-sizing:border-box;margin:0;padding:0}
html,body{width:1200px;height:748px;overflow:hidden}
body{background:var(--page);font-family:"Roboto",sans-serif;color:var(--ink);position:relative}
.abs{position:absolute}

/* sidebar */
.sidebar{position:absolute;left:0;top:0;width:176px;height:748px;background:var(--side)}
.org-switch{position:absolute;left:0;top:0;width:176px;height:37px;background:var(--side-dark);display:flex;align-items:center;padding-left:21px;gap:6px;color:#fff;font-size:12px}
.org-dot{width:20px;height:20px;border-radius:50%;background:var(--orange)}
.nav-item{position:absolute;left:42px;width:92px;height:48px;display:flex;flex-direction:column;align-items:center;justify-content:flex-end;padding-bottom:4px;gap:5px;font-size:10px;color:var(--nav-label)}
.nav-item.active{background:var(--side-active);color:#fff;font-weight:700;border-radius:2px}
.nav-item svg{width:22px;height:22px}
.powered{position:absolute;left:35px;top:687px;width:105px;height:50px;background:var(--side-dark);padding:7px 8px}
.powered small{display:block;font-size:6px;color:#2c7c86}
.powered strong{display:flex;align-items:center;gap:5px;margin-top:7px;font-size:13px;font-weight:500;color:#dfe9ea}
.powered strong i{width:10px;height:10px;border-radius:50%;background:#2c8fa0;display:block}

/* header */
.lang{left:990px;top:20px;font-size:16px;color:var(--teal-ink);display:flex;align-items:center;gap:8px}
.avatar{border-radius:50%;background:linear-gradient(135deg,#c7a28b,#6d4a3c)}
.user{left:1124px;top:21px}
.user b{display:block;font-size:12px;color:var(--teal-ink)}
.user span{font-size:11px;color:var(--muted)}
.greet{left:207px;top:58px;font-size:20px;font-weight:700;color:#595959;line-height:23px}
.greet em{font-style:normal;color:var(--teal-ink)}
.greet span{display:block;color:#cfcfcf}

/* cards */
.card{position:absolute;background:var(--card);border-radius:8px}
.card-title{position:absolute;font-size:12px;font-weight:700;color:#4a4a4a}
.shadow{box-shadow:0 6px 14px rgba(0,0,0,.08)}

.event-panel{left:119px;top:36px;width:99px;height:148px;background:var(--orange-soft);border-radius:4px;text-align:center}
.clock{font-size:26px;font-weight:700;position:absolute;top:88px;left:0;right:0}
.checked{font-size:10px;color:var(--orange);font-weight:500;position:absolute;top:118px;left:18px}

.cal{position:absolute;left:255px;top:42px;display:grid;grid-template-columns:repeat(7,34px);row-gap:7px;font-size:11px;text-align:center}
.cal span{height:16px;line-height:16px;position:relative}
.cal .hd{color:#777}
.cal .off{color:var(--soft)}
.cal .mk{font-weight:700}
.cal .mk::after{content:"";position:absolute;left:11px;right:11px;bottom:-3px;height:2px;border-radius:1px;background:var(--orange)}
.cal .mk.b::after{background:var(--blue)}

.big{font-size:24px;font-weight:700}
.btn{position:absolute;left:14px;top:137px;width:190px;height:38px;background:var(--orange);color:#fff;border-radius:8px;font-size:12px;font-weight:700;display:flex;align-items:center;justify-content:center}

.tardy-row{position:absolute;left:16px;width:198px;height:44px;border-bottom:1px solid var(--line);display:flex;align-items:center}
.tardy-row .avatar{width:34px;height:34px}
.tardy-row div{margin-left:11px;font-size:12px;line-height:15px;flex:1}
.tardy-row b{font-weight:700}
.tardy-row p{color:var(--muted)}
.score{color:var(--orange);font-weight:700;font-size:12px;margin-right:5px}

.filter{position:absolute;top:14px;font-size:10px;color:var(--muted)}
.pill{background:#eee;color:var(--ink);border-radius:9px;padding:3px 6px}
.leave-card{position:absolute;left:14px;top:45px;width:148px;height:108px;border:1px solid var(--line);border-radius:4px;padding:12px 9px}
.leave-card .avatar{width:34px;height:34px;background:linear-gradient(135deg,#6a2a2a,#1e1414)}
.leave-card b{display:block;margin-top:7px;font-size:12px}
.leave-card p{font-size:12px;color:var(--muted)}
.badge{display:inline-block;margin-top:4px;border:1px solid var(--orange);color:var(--orange);border-radius:6px;font-size:6px;padding:1px 6px}

.ql{position:absolute;left:15px}
.ql b{display:block;font-size:20px;font-weight:700}
.ql span{font-size:10px;font-weight:700;color:#666}

.feed{position:absolute;height:46px;border:1px solid var(--line);border-radius:6px;display:flex;align-items:center;font-size:12px}
.feed svg{width:16px;height:16px;margin:0 17px 0 15px}
</style>
</head>
<body>

<aside class="sidebar">
  <div class="org-switch"><span class="org-dot"></span>PT Reed Manufact..
    <svg width="10" height="8" viewBox="0 0 10 8"><path d="M1 2l4 4 4-4" stroke="#f37122" stroke-width="2" fill="none"/></svg></div>
  <div class="nav-item active" style="top:58px"><svg viewBox="0 0 24 24"><path d="M3 17a9 9 0 0118 0z" fill="#f3d9a9"/><path d="M12 16l5-6" stroke="#f37122" stroke-width="2"/></svg>Dashboard</div>
  <div class="nav-item" style="top:111px"><svg viewBox="0 0 24 24" fill="var(--nav-icon)"><circle cx="12" cy="8" r="4"/><circle cx="5" cy="10" r="3"/><circle cx="19" cy="10" r="3"/><path d="M4 20a8 6 0 0116 0z"/></svg>Employees</div>
  <div class="nav-item" style="top:163px"><svg viewBox="0 0 24 24"><rect x="3" y="5" width="18" height="16" rx="2" fill="var(--nav-icon)"/><path d="M7 11h2M11 11h2M15 11h2M7 15h2M11 15h2M15 15h2" stroke="#fff" stroke-width="2"/></svg>Calendar</div>
  <div class="nav-item" style="top:216px"><svg viewBox="0 0 24 24"><path d="M5 2h10l4 4v16H5z" fill="var(--nav-icon)"/><text x="12" y="17" font-size="9" text-anchor="middle" fill="#fff">$</text></svg>Expenses</div>
  <div class="nav-item" style="top:268px"><svg viewBox="0 0 24 24"><rect x="2" y="8" width="20" height="12" rx="1" fill="var(--nav-icon)"/><path d="M8 4l10 10" stroke="#fff" stroke-width="2"/></svg>Payroll</div>
  <div class="nav-item" style="top:321px"><svg viewBox="0 0 24 24"><path d="M3 10l9-7 9 7v11H3z" fill="var(--nav-icon)"/><circle cx="12" cy="12" r="4" fill="#fff"/></svg>Loans</div>
  <div class="nav-item" style="top:374px"><svg viewBox="0 0 24 24" fill="var(--nav-icon)"><rect x="3" y="13" width="3" height="8"/><rect x="8" y="10" width="3" height="11"/><rect x="13" y="12" width="3" height="9"/><rect x="18" y="8" width="3" height="13"/><path d="M3 9l5-4 5 3 7-6" stroke="var(--nav-icon)" stroke-width="2" fill="none"/></svg>Performance</div>
  <div class="nav-item" style="top:426px"><svg viewBox="0 0 24 24"><circle cx="12" cy="12" r="7" stroke="var(--nav-icon)" stroke-width="3" fill="none"/><path d="M12 2v6M12 16v6M2 12h6M16 12h6" stroke="var(--nav-icon)" stroke-width="2"/></svg>Engagement</div>
  <div class="nav-item" style="top:479px"><svg viewBox="0 0 24 24"><path d="M5 2h10l4 4v16H5z" fill="var(--nav-icon)"/><circle cx="12" cy="14" r="4" fill="#fff"/></svg>Reports</div>
  <div class="nav-item" style="top:531px"><svg viewBox="0 0 24 24"><circle cx="12" cy="12" r="8" fill="var(--nav-icon)" stroke="var(--nav-icon)" stroke-width="4" stroke-dasharray="3 2.3"/><circle cx="12" cy="12" r="3" fill="var(--side)"/></svg>Settings</div>
  <div class="powered"><small>Powered by</small><strong><i></i>QuillStaff</strong></div>
</aside>

<div class="abs lang">English <svg width="12" height="8" viewBox="0 0 12 8"><path d="M1 1l5 5 5-5" stroke="#aaa" stroke-width="1.5" fill="none"/></svg></div>
<div class="abs avatar" style="left:1087px;top:20px;width:31px;height:31px" role="img" aria-label="Profile photo of the signed-in admin"></div>
<div class="abs user"><b>Marisol HR</b><span>Admin</span></div>

<h1 class="abs greet">Good Morning <em>Daniel,</em><span>its good to see you again</span></h1>

<section class="card shadow" style="left:206px;top:125px;width:227px;height:195px">
  <h2 class="card-title" style="left:11px;top:10px">Today's event</h2>
  <p class="abs" style="left:11px;top:42px;font-size:10px;font-weight:500;color:#333">Tue, 26 May 20</p>
  <p class="abs" style="left:11px;top:60px;font-size:13px;font-weight:700">09:00 to 18:00</p>
  <p class="abs" style="left:11px;top:116px;font-size:10px;color:#555">Working</p>
  <p class="abs" style="left:11px;top:131px;font-size:13px;font-weight:700">Branch B</p>
  <div class="abs event-panel">
    <svg class="abs" style="left:25px;top:22px" width="54" height="54" viewBox="0 0 54 54"><circle cx="27" cy="27" r="23" stroke="#f9cfa6" stroke-width="4" fill="none" stroke-dasharray="120 200" transform="rotate(-60 27 27)"/><path d="M27 4a23 23 0 0118 9" stroke="var(--orange)" stroke-width="5" fill="none" stroke-linecap="round"/></svg>
    <div class="clock">08:50</div>
    <div class="checked">Checked in</div>
  </div>
</section>

<section class="card" style="left:451px;top:125px;width:491px;height:195px">
  <h2 class="card-title" style="left:17px;top:15px">My Schedule</h2>
  <div class="abs" style="left:427px;top:14px;font-size:12px;font-weight:700;display:flex;gap:9px;align-items:center">May <svg width="10" height="7" viewBox="0 0 10 7"><path d="M1 1l4 4 4-4" stroke="#888" stroke-width="1.5" fill="none"/></svg></div>
  <div class="abs" style="left:16px;top:42px;color:#666;font-size:12px;line-height:14px">May<br><span style="font-size:20px;line-height:22px">26</span></div>
  <div class="abs" style="left:64px;top:45px;width:1px;height:32px;background:var(--line)"></div>
  <div class="abs" style="left:82px;top:42px;font-size:12px;line-height:19px"><b>09:00 to 18:00</b><br><span style="color:#555">Working Branch B</span></div>
  <div class="abs" style="left:16px;top:104px;color:#666;font-size:12px;line-height:14px">May<br><span style="font-size:20px;line-height:22px">28</span></div>
  <div class="abs" style="left:64px;top:107px;width:1px;height:32px;background:var(--line)"></div>
  <div class="abs" style="left:82px;top:104px;font-size:12px;line-height:19px"><b>10:00 to 12:00</b><br><span style="color:#555">Working Branch A</span></div>
  <div class="cal">
    <span class="hd">M</span><span class="hd">T</span><span class="hd">W</span><span class="hd">T</span><span class="hd">F</span><span class="hd">S</span><span class="hd">S</span>
    <span class="off">31</span><span>01</span><span>02</span><span>03</span><span>04</span><span class="off">05</span><span class="off">06</span>
    <span>07</span><span>08</span><span class="mk">09</span><span>10</span><span>11</span><span class="off">12</span><span class="off">13</span>
    <span>14</span><span>15</span><span>16</span><span class="mk b">17</span><span>18</span><span class="off">19</span><span class="off">20</span>
    <span>21</span><span class="mk b">22</span><span>23</span><span>24</span><span>25</span><span class="off">26</span><span class="off">27</span>
    <span>28</span><span>28</span><span class="mk">30</span><span class="off">01</span><span class="off">02</span><span class="off">03</span><span class="off">04</span>
  </div>
</section>

<section class="card" style="left:958px;top:125px;width:221px;height:195px">
  <h2 class="card-title" style="left:15px;top:14px">My Time off</h2>
  <div class="abs" style="left:15px;top:60px;font-size:11px">Left<div class="big">06</div><span style="font-size:12px;color:var(--soft);font-weight:500">Annual leave</span></div>
  <div class="abs" style="left:109px;top:62px;width:1px;height:49px;background:var(--line)"></div>
  <div class="abs" style="left:133px;top:60px;font-size:11px">Taken<div class="big">01</div><span style="font-size:12px;color:var(--soft);font-weight:500">Sick days</span></div>
  <div class="btn">Request</div>
</section>

<section class="card" style="left:207px;top:337px;width:221px;height:180px">
  <h2 class="card-title" style="left:16px;top:13px">Tardy today</h2>
  <div class="tardy-row" style="top:46px"><span class="avatar" role="img" aria-label="Employee photo"></span><div><b>79, Employee</b><p>Logistic Officer</p></div><span class="score">7.0</span></div>
  <div class="tardy-row" style="top:90px"><span class="avatar" role="img" aria-label="Employee photo"></span><div><b>79, Employee</b><p>Logistic Officer</p></div><span class="score">7.0</span></div>
</section>

<section class="card" style="left:446px;top:338px;width:496px;height:179px">
  <h2 class="card-title" style="left:14px;top:15px">Who's on leave today</h2>
  <span class="filter" style="left:234px">Filter :</span>
  <span class="filter pill" style="left:277px;top:11px">Department</span>
  <span class="filter" style="left:368px">Branch</span>
  <span class="filter" style="left:421px">Subordinates</span>
  <div class="leave-card">
    <span class="avatar" style="display:block" role="img" aria-label="Employee photo"></span>
    <b>79, Employee</b><p>HR Administrator</p>
    <span class="badge">Maternity leave</span>
  </div>
</section>

<section class="card" style="left:958px;top:336px;width:221px;height:181px">
  <h2 class="card-title" style="left:15px;top:12px">Quicklinks</h2>
  <div class="ql" style="top:36px"><b>12</b><span>Event Amandements</span></div>
  <div class="ql" style="top:80px"><b>02</b><span>Leave Requests</span></div>
  <div class="ql" style="top:127px"><b>07</b><span>Event Requests</span></div>
</section>

<section class="card" style="left:206px;top:534px;width:548px;height:182px">
  <h2 class="card-title" style="left:17px;top:27px">Who's on leave today</h2>
  <div class="feed" style="left:17px;top:60px;width:515px"><svg viewBox="0 0 16 16"><rect x="1.5" y="3" width="13" height="11.5" rx="1" stroke="#bbb" fill="none"/><path d="M1.5 6h13M5 1.5v3M11 1.5v3" stroke="#bbb"/><rect x="7" y="9" width="3" height="3" fill="#bbb"/></svg>Wirawan, Laras has remotely checked in for Working on 20/05/2020 02:07</div>
  <div class="feed" style="left:17px;top:114px;width:515px"><svg viewBox="0 0 16 16"><rect x="1.5" y="3" width="13" height="11.5" rx="1" stroke="#bbb" fill="none"/><path d="M1.5 6h13M5 1.5v3M11 1.5v3" stroke="#bbb"/><rect x="7" y="9" width="3" height="3" fill="#bbb"/></svg>Overtime request for Wirawan, Laras - 18 May 2020 at 19:00 | 21:00 Branch A</div>
</section>

<section class="card" style="left:768px;top:537px;width:409px;height:183px">
  <h2 class="card-title" style="left:14px;top:15px">Who's on leave today</h2>
  <div class="feed" style="left:15px;top:48px;width:370px"><svg viewBox="0 0 16 16"><rect x="1.5" y="3" width="13" height="11.5" rx="1" stroke="#bbb" fill="none"/><path d="M1.5 6h13M5 1.5v3M11 1.5v3" stroke="#bbb"/><rect x="7" y="9" width="3" height="3" fill="#bbb"/></svg>Wirawan, Laras has remotely checked in for Working</div>
  <div class="feed" style="left:15px;top:102px;width:370px"><svg viewBox="0 0 16 16"><rect x="1.5" y="3" width="13" height="11.5" rx="1" stroke="#bbb" fill="none"/><path d="M1.5 6h13M5 1.5v3M11 1.5v3" stroke="#bbb"/><rect x="7" y="9" width="3" height="3" fill="#bbb"/></svg>Overtime request for Wirawan, Laras - 18 May 2020</div>
</section>

</body>
</html>
```